logo and label design for a vegan skincare Called Leafmerelle

We need a logo and label design for a skincare brand called leafmerelle based in Australia. The products are 100% natural, Australian made, small batch, vegan, cruelty-free, ethical and sustainable beauty products. The secret of our skin care products are their naturally active ingredients.
They are potent, yet incredibly gentle on sensitive skin. We believe in investing in only the highest quality and ethical ingredients to ensure we are creating products we can stand behind.
Our products use: Naturally delivered ingredients; Organic ingredients where is possible; Australian oils, fruits & Extracts; Aromatherapy oils; sustainable & ethical ingredients; natural preservatives.
Our products don't use: sulphates; parabens; phthalates; Petrochemicals; synthetic colours; synthetic fragrances. All label must be design for an amber bottle.
Label Requirements:
* 300 DPI minimum
* All fonts have been outlined
* 3mm Bleed included in artwork
Colors
Designer to choose colors to be used in the design.
Look and feel
Each slider illustrates characteristics of the customer's brand and the style your logo design should communicate.

```html
<!DOCTYPE html>
<html lang="en">
<head>
<meta charset="utf-8">
<title>Leafmerelle – Purifying Gel Cleanser Label</title>
<link href="https://fonts.googleapis.com/css2?family=Bebas+Neue&family=Montserrat:wght@500&family=Open+Sans:wght@400&family=Yesteryear&display=swap" rel="stylesheet">
<style>
  :root {
    --page: #ffffff;
    --label-light: #d9cdbf;
    --label-dark: #beb2a3;
    --edge: #e6ddd2;
    --ink: #0d0d0d;
    --rule: #2a2622;
  }
  html, body {
    margin: 0;
    width: 1200px;
    height: 1200px;
    overflow: hidden;
    background: var(--page);
  }
  .label {
    position: absolute;
    left: 220px;
    top: 105px;
    width: 760px;
    height: 990px;
    background: linear-gradient(90deg, var(--label-light) 0%, #d3c7b8 55%, var(--label-dark) 100%);
    color: var(--ink);
    text-align: center;
  }
  .label__edge {
    position: absolute;
    left: 0; right: 0;
    background: var(--edge);
  }
  .label__edge--top { top: 0; height: 22px; }
  .label__edge--bottom { bottom: 0; height: 18px; }
  .label__band {
    position: absolute;
    left: 0; right: 0;
    height: 19px;
    background: var(--ink);
  }
  .label__band--top { top: 22px; }
  .label__band--bottom { top: 949px; height: 23px; }
  .brand-mark {
    position: absolute;
    left: 310px;
    top: 41px;
    width: 141px;
    height: 128px;
    background: var(--ink);
  }
  .brand-name {
    position: absolute;
    left: 0; right: 0;
    top: 178px;
    font-family: "Montserrat", sans-serif;
    font-weight: 500;
    font-size: 66px;
    letter-spacing: 2px;
    line-height: 1;
  }
  .product-name {
    position: absolute;
    left: 0; right: 0;
    top: 366px;
    margin: 0;
    font-family: "Bebas Neue", sans-serif;
    font-weight: 400;
    font-size: 96px;
    line-height: 90px;
    letter-spacing: 1px;
  }
  .rule {
    position: absolute;
    left: 126px;
    width: 524px;
    height: 2px;
    background: var(--rule);
  }
  .rule--upper { top: 560px; }
  .rule--lower { top: 652px; }
  .ingredients {
    position: absolute;
    left: 0; right: 0;
    top: 574px;
    font-family: "Yesteryear", cursive;
    font-size: 46px;
    line-height: 60px;
  }
  .dots {
    position: absolute;
    left: 0; right: 0;
    font-family: "Open Sans", sans-serif;
    font-size: 22px;
    letter-spacing: 3px;
    line-height: 1;
  }
  .dots--upper { top: 660px; }
  .dots--lower { top: 868px; }
  .claim {
    position: absolute;
    left: 0; right: 0;
    top: 690px;
    font-family: "Bebas Neue", sans-serif;
    font-size: 50px;
    letter-spacing: 3px;
    line-height: 1;
  }
  .badges {
    position: absolute;
    left: 150px;
    top: 752px;
    width: 460px;
    height: 110px;
  }
  .volume {
    position: absolute;
    left: 0; right: 0;
    top: 888px;
    font-family: "Open Sans", sans-serif;
    font-size: 36px;
    line-height: 1;
  }
</style>
</head>
<body>
  <main class="label">
    <div class="label__edge label__edge--top"></div>
    <div class="label__band label__band--top"></div>

    <div class="brand-mark"></div>
    <div class="brand-name">LEAFMERELLE</div>

    <h1 class="product-name">Purifying<br>Gel Cleanser</h1>

    <div class="rule rule--upper"></div>
    <div class="ingredients">· Lemon Tea Tree &amp; Vitamim E ·</div>
    <div class="rule rule--lower"></div>

    <div class="dots dots--upper">• • •</div>
    <div class="claim">NATURAL</div>

    <svg class="badges" viewBox="0 0 460 110" aria-label="Vegan, all natural, cruelty free and Australian made badges">
      <g fill="none" stroke="#0d0d0d" stroke-width="4">
        <circle cx="48" cy="56" r="40"/>
        <circle cx="168" cy="50" r="40"/>
        <circle cx="290" cy="50" r="40"/>
      </g>
      <polygon points="410,6 458,96 362,96" fill="#0d0d0d"/>
    </svg>

    <div class="dots dots--lower">• • •</div>
    <div class="volume">200 ml</div>

    <div class="label__band label__band--bottom"></div>
    <div class="label__edge label__edge--bottom"></div>
  </main>
</body>
</html>
```